Business Card Design

We are state certified residental contractors who specialize in insurance claims. We are insurance restoration experts and have a state multi-lines insurance adjusters license #W581403. We produce insurance grade estimates using the most widely used software in the industry. Our goal is to work for our customers! not the insurance company. Our edge is we don't take short cuts to please the adjuster/insurance company to insure future claims from them. We are experts at restoring damaged properties.from wind, water ,fire and smoke. We pride ourselfs on evaluating damages properly and providing extremely detailed estimates for restoration.We are also educated and experienced in identifiying and correcting indoor air quality issues as a result of common perils and defective materials. .We are not a franchise and are family owned and operated. We provide quality work using only the best local tradesman. We ourselfs are local tradesmen and helped build and restore our community over the past 30 years. We know first hand how our homes were built and are aware of many of the common problems that exist and how to address them. We are licensed insured and bonded.
Industry/Entity Type
Business
Contact Information for Business Card
Harbor Keystone LLC
Martin Calloway
4175 Pelican Rd unit K
Melbourne Fl.32815 Manager/State Certified Residental Contractor license# CRC1846052
321-555-0174 Office
321-555-0188 Fax

```html
<!DOCTYPE html>
<html lang="en">
<head>
<meta charset="utf-8">
<title>Harbor Keystone LLC – Business Card</title>
<link href="https://fonts.googleapis.com/css2?family=Roboto+Condensed:wght@400;700&display=swap" rel="stylesheet">
<style>
  :root {
    --red: #b5121b;
    --red-dark: #9e0f17;
    --ink: #2b2b2d;
    --black: #1e1e20;
    --paper: #ffffff;
    --backdrop: #e9e9ea;
  }
  * { box-sizing: border-box; margin: 0; padding: 0; }
  html, body {
    width: 1200px; height: 892px; overflow: hidden;
    background: var(--backdrop);
    font-family: "Roboto Condensed", "Arial Narrow", sans-serif;
  }
  .sheet { position: relative; width: 1200px; height: 892px; }
  .card {
    position: absolute; left: 290px; width: 620px; height: 354px;
    background: var(--paper); overflow: hidden;
    box-shadow: 0 6px 18px rgba(0,0,0,.18);
  }
  .card--front { top: 60px; }
  .card--back { top: 474px; }
  .card__waves { position: absolute; inset: 0; width: 100%; height: 100%; }

  .brand-name {
    position: relative;
    color: var(--red); font-weight: 700; text-transform: uppercase;
    letter-spacing: .5px; line-height: 1;
  }
  .card--front .brand-name {
    position: absolute; left: 44px; top: 30px; font-size: 40px;
  }
  .contact {
    position: absolute; left: 46px; top: 84px; color: var(--ink);
  }
  .contact__name {
    font-size: 26px; font-weight: 700; text-transform: uppercase; line-height: 1.05;
  }
  .contact__title { font-size: 14px; line-height: 1.3; }
  .contact__license { font-size: 14px; color: var(--red); line-height: 1.3; }
  .contact__lines { margin-top: 8px; list-style: none; }
  .contact__line {
    display: flex; align-items: center; gap: 10px;
    font-size: 18px; line-height: 1.35;
  }
  .contact__icon { width: 16px; height: 16px; flex: none; }
  .address {
    position: absolute; left: 44px; bottom: 18px;
    color: var(--paper); font-size: 19px;
  }

  .card--back .brand-name {
    position: absolute; left: 0; right: 0; top: 92px;
    text-align: center; font-size: 54px;
  }
</style>
</head>
<body>
<main class="sheet">

  <section class="card card--front" aria-label="Card front">
    <svg class="card__waves" viewBox="0 0 620 354" preserveAspectRatio="none" aria-hidden="true">
      <path fill="var(--black)" d="M0,234 C200,238 380,272 620,282 L620,326 C380,308 180,246 0,242 Z"/>
      <path fill="var(--red)" d="M0,250 C180,254 380,316 620,334 L620,354 L0,354 Z"/>
    </svg>
    <h1 class="brand-name">Harbor Keystone LLC</h1>
    <div class="contact">
      <p class="contact__name">Martin Calloway</p>
      <p class="contact__title">Manager / State Certified Residental Contractor</p>
      <p class="contact__license">license# CRC1846052</p>
      <ul class="contact__lines">
        <li class="contact__line">
          <svg class="contact__icon" viewBox="0 0 16 16" aria-label="Office">
            <rect width="16" height="16" rx="3" fill="var(--red)"/>
            <path fill="#fff" d="M5 3.5l1.6 2.2-1 1.1c.6 1.3 1.4 2.1 2.6 2.7l1.1-1L11.5 10 10.6 12C7 11.6 4.4 9 4 5.4Z"/>
          </svg>
          <span>321-555-0174</span>
        </li>
        <li class="contact__line">
          <svg class="contact__icon" viewBox="0 0 16 16" aria-label="Fax">
            <rect width="16" height="16" rx="3" fill="var(--red)"/>
            <rect x="5" y="3" width="6" height="3" fill="#fff"/>
            <rect x="3" y="6.5" width="10" height="5" rx="1" fill="#fff"/>
            <rect x="5" y="10" width="6" height="3" fill="#fff"/>
          </svg>
          <span>321-555-0188</span>
        </li>
      </ul>
    </div>
    <p class="address">4175 Pelican Rd unit K Melbourne Fl.32815</p>
  </section>

  <section class="card card--back" aria-label="Card back">
    <svg class="card__waves" viewBox="0 0 620 354" preserveAspectRatio="none" aria-hidden="true">
      <path fill="var(--black)" d="M0,208 C150,196 320,236 620,252 L620,260 C350,260 150,268 0,276 Z"/>
      <path fill="var(--red)" d="M0,284 C200,276 400,268 620,270 L620,354 L0,354 Z"/>
    </svg>
    <h2 class="brand-name">Harbor Keystone LLC</h2>
  </section>

</main>
</body>
</html>
```